依頼詳細
建設業界では、まだ段階の世代で古き良き
日本というカテゴリが強く残っている現状ですが
大手スーパーゼネコンのように、現代の最先端のユーモアさも取り入れ
他の建設業界とは、一風変わった特徴ある名刺を作成したいと
考えて応募しました。
記載項目
株式会社 DAVRO
代表取締役 高野 典久
希望イメージ
シンプル 複雑
単色 カラフル
暗い 明るい
日常 高級
遊び心 厳粛
未来的 伝統的
女性的 男性的
希望する色
オレンジ
納品ファイル
• 高解像度JPG (.jpg)
• フォトショップ形式 (.psd)
補足説明
当社のロゴのdataを追加しました。

ですが必ずしもロゴを記載したいというわけではございません
自分自身は趣味でヨーロッパなどの歴史ある建造物などを
見に足を運ぶなどもしております。(^^)
■ 選んだ理由

横のデザイン構成・全体的なバランス
がとても気に入り決断致しました。

■ 提案者全員のお礼・コメント

この度は皆様方に
様々なご提案、ご参加いただき
誠にお礼を申し上げる次第です。

ありがとうございます。

```html
<!DOCTYPE html>
<html lang="ja">
<head>
<meta charset="UTF-8">
<title>株式会社 DAVRO 名刺</title>
<link href="https://fonts.googleapis.com/css2?family=Noto+Sans+JP:wght@400;700&family=Noto+Serif+JP:wght@400;500&display=swap" rel="stylesheet">
<style>
  :root {
    --orange: #f08a1c;
    --orange-deep: #e2620f;
    --orange-faint: rgba(240, 138, 28, 0.12);
    --ink: #1e1e1e;
    --paper: #ffffff;
  }
  html, body {
    margin: 0;
    padding: 0;
    width: 794px;
    height: 1200px;
    overflow: hidden;
    background: var(--paper);
  }
  .card {
    position: relative;
    width: 794px;
    height: 1200px;
    background: var(--paper);
    font-family: "Noto Sans JP", sans-serif;
    color: var(--ink);
    overflow: hidden;
  }
  .accent-bar {
    position: absolute;
    background: var(--orange);
  }
  .accent-bar--right { left: 752px; top: 58px; width: 22px; height: 550px; }
  .accent-bar--left { left: 10px; top: 660px; width: 22px; height: 500px; }

  .backdrop-mark {
    position: absolute;
    left: 430px;
    top: 380px;
    width: 360px;
    height: 360px;
    border-radius: 50%;
    background: var(--orange-faint);
  }

  .brand {
    position: absolute;
    left: 60px;
    top: 90px;
    display: flex;
    flex-direction: column;
    align-items: flex-start;
  }
  .brand__dot {
    width: 300px;
    height: 300px;
    border-radius: 50%;
    background: var(--orange);
    opacity: 0.9;
  }
  .brand__name {
    margin-top: 40px;
    font-size: 64px;
    font-weight: 700;
    color: var(--orange-deep);
    letter-spacing: 2px;
    line-height: 1;
  }
  .brand__url {
    margin-top: 16px;
    font-size: 24px;
    font-weight: 700;
    color: var(--orange-deep);
  }

  .person {
    position: absolute;
    writing-mode: vertical-rl;
    font-family: "Noto Serif JP", serif;
  }
  .person__title { left: 515px; top: 205px; font-size: 38px; letter-spacing: 4px; }
  .person__name { left: 590px; top: 330px; font-size: 66px; font-weight: 500; letter-spacing: 8px; }
  .person__roman {
    left: 690px; top: 205px;
    font-family: "Noto Sans JP", sans-serif;
    font-size: 18px;
    letter-spacing: 3px;
    color: #8a8a8a;
  }

  .contact {
    position: absolute;
    left: 58px;
    top: 845px;
    font-size: 27px;
    line-height: 1.55;
  }
  .contact__company { font-weight: 700; font-size: 31px; margin: 0 0 4px; }
  .contact__line { margin: 0; }
  .contact__line--accent { color: var(--orange-deep); }
</style>
</head>
<body>
  <div class="card">
    <div class="accent-bar accent-bar--right"></div>
    <div class="accent-bar accent-bar--left"></div>
    <div class="backdrop-mark"></div>

    <div class="brand">
      <div class="brand__dot"></div>
      <div class="brand__name">DAVRO</div>
      <div class="brand__url">http://www.davro.co.jp</div>
    </div>

    <div class="person person__title">代表取締役</div>
    <div class="person person__name">高野 典久</div>
    <div class="person person__roman">Norihisa Takano</div>

    <div class="contact">
      <p class="contact__company">株式会社 DAVRO</p>
      <p class="contact__line">〒123-4567 東京都○○○区○○○町1-1-1</p>
      <p class="contact__line contact__line--accent">Tel:03-0000-0000　Fax:03-0000-0000</p>
      <p class="contact__line contact__line--accent">E-mail:○○○○@.com○○○○</p>
    </div>
  </div>
</body>
</html>
```